Business Card Design

new real estate company in the Colorado mountains would like fun..creative.. pines trees and house and dog(s)? heart? I love colors

I am also asking for a logo design then to biz cards..

Industry/Entity Type

Real Estate

Contact Information for Business Card

Meadowlark Bend Realty

Rosalind Tavers
"Your Mountain Home Starts Here!"
555-316-0847
rosalindmtavers@brightpost.example

```html
<!DOCTYPE html>
<html lang="en">
<head>
<meta charset="utf-8">
<title>Meadowlark Bend Realty – Business Card</title>
<link rel="stylesheet" href="https://fonts.googleapis.com/css2?family=Cinzel:wght@500&family=Sorts+Mill+Goudy:ital@1&family=Questrial&display=swap">
<style>
  :root {
    --page-bg: #f3f4f4;
    --card-white: #ffffff;
    --card-mist: #e6e9ea;
    --teal-dark: #123a40;
    --teal: #1f5b63;
    --teal-text: #24606a;
    --ink: #1c2426;
    --silver: #c9cfd1;
    --night-top: #0e2a30;
    --night-mid: #1d4c55;
    --night-glow: #3d7480;
    --mark-teal: #2b6670;
    --back-text: #e9eef0;
  }
  * { margin: 0; padding: 0; box-sizing: border-box; }
  html, body { width: 1200px; height: 900px; overflow: hidden; }
  body { background: var(--page-bg); position: relative; }

  .card {
    position: absolute;
    top: 290px;
    width: 540px;
    height: 310px;
    border-radius: 22px;
    overflow: hidden;
    box-shadow: 0 10px 28px rgba(0, 0, 0, 0.14);
  }

  /* Front of card */
  .card-front {
    left: 40px;
    background: linear-gradient(160deg, var(--card-white) 0%, var(--card-white) 45%, var(--card-mist) 100%);
  }
  .brand-square {
    position: absolute;
    left: 22px; top: 30px;
    width: 84px; height: 84px;
    border-radius: 8px;
    background: var(--mark-teal);
    border: 2px solid var(--silver);
  }
  .front-name {
    position: absolute;
    left: 122px; top: 40px;
    font-family: "Cinzel", serif;
    font-weight: 500;
    font-size: 27px;
    color: var(--ink);
    white-space: nowrap;
  }
  .tagline {
    position: absolute;
    left: 168px; top: 84px;
    font-family: "Sorts Mill Goudy", serif;
    font-style: italic;
    font-size: 17px;
    color: var(--teal-text);
    white-space: nowrap;
  }
  .agent-name {
    position: absolute;
    left: 20px; top: 158px;
    font-family: "Questrial", sans-serif;
    font-size: 21px;
    font-weight: 400;
    color: var(--teal-text);
  }
  .contact-list {
    position: absolute;
    left: 22px; top: 200px;
    list-style: none;
    font-family: "Questrial", sans-serif;
    font-size: 17px;
    color: var(--ink);
  }
  .contact-list li { display: flex; align-items: center; gap: 8px; height: 25px; white-space: nowrap; }
  .contact-list svg { width: 14px; height: 14px; fill: var(--teal); flex: none; }
  .front-band {
    position: absolute;
    left: 0; right: 0; bottom: 0;
    height: 34px;
    background: linear-gradient(180deg, var(--teal) 0%, var(--teal-dark) 100%);
    border-top: 4px solid var(--silver);
  }

  /* Back of card */
  .card-back { left: 620px; }
  .night-scene {
    position: absolute; inset: 0;
    background:
      radial-gradient(ellipse at 40% 45%, var(--night-glow) 0%, transparent 55%),
      linear-gradient(180deg, var(--night-mid) 0%, var(--night-top) 70%, #0a1f23 100%);
  }
  .back-square {
    position: absolute;
    left: 200px; top: 40px;
    width: 160px; height: 160px;
    border-radius: 14px;
    background: var(--mark-teal);
    border: 3px solid var(--silver);
  }
  .back-name {
    position: absolute;
    left: 0; right: 0; top: 234px;
    text-align: center;
    font-family: "Cinzel", serif;
    font-weight: 500;
    font-size: 25px;
    color: var(--back-text);
    white-space: nowrap;
  }
</style>
</head>
<body>

  <section class="card card-front" aria-label="Business card front">
    <div class="brand-square"></div>
    <h1 class="front-name">Meadowlark Bend Realty</h1>
    <p class="tagline">“Your Mountain Home Starts Here!”</p>
    <h2 class="agent-name">Rosalind Tavers</h2>
    <ul class="contact-list">
      <li>
        <svg viewBox="0 0 24 24" aria-hidden="true"><path d="M6.6 10.8a15.1 15.1 0 0 0 6.6 6.6l2.2-2.2a1 1 0 0 1 1-.25 11.4 11.4 0 0 0 3.6.57 1 1 0 0 1 1 1V20a1 1 0 0 1-1 1A17 17 0 0 1 3 4a1 1 0 0 1 1-1h3.5a1 1 0 0 1 1 1c0 1.25.2 2.45.57 3.57a1 1 0 0 1-.25 1z"/></svg>
        555-316-0847
      </li>
      <li>
        <svg viewBox="0 0 24 24" aria-hidden="true"><path d="M2 6h20v12H2z M2 6l10 7 10-7" fill="none" stroke="#1f5b63" stroke-width="2.4"/></svg>
        rosalindmtavers@brightpost.example
      </li>
    </ul>
    <div class="front-band"></div>
  </section>

  <section class="card card-back" aria-label="Business card back">
    <div class="night-scene" role="img" aria-label="Night sky with stars over a dark pine forest"></div>
    <div class="back-square"></div>
    <h2 class="back-name">Meadowlark Bend Realty</h2>
  </section>

</body>
</html>
```